Retail Package Design for Consumer Product Goods (soup)

Company is in need of food package design (front and back). Product will be in a stand-up pouch-type packaging. Size is 10.4 inch (vertical) by 7.65 inch (horizontal). Product is for retail sales, so design needs to be eye catching. It's considered more healthy food, so would like the design to be communicate health.
Target Market(s)
Natural healthy food
Industry/Entity Type
Retail
Requirements
Must have
- Must be done in Illustrator.
FRONT:
Clean, simple design that communicates premium and healthy food. Name of Product is "Duck & Barley Soup" with subtitle of "Made with Organic Seaweed"
- Callouts somewhere on the package: "Traditional Korean-Style Soup", "Fully Cooked, Ready in Minutes", and "Beef used raised with no hormones & antibiotics".
- Bottom of package should say "Net Wt. 2 LBs (32oz)" and "Keep Refrigerated".
BACKSIDE
- See attached document "Content for Backside" for content: Nutrition Fact, Ingredient List, Place for a bar code, brief summary of the product
Nice to have
- would like to see rendering of pouch

```html
<!DOCTYPE html>
<html lang="en">
<head>
<meta charset="utf-8">
<title>Duck &amp; Barley Soup – Pouch Front</title>
<link rel="stylesheet" href="https://fonts.googleapis.com/css2?family=Fredoka:wght@500;600;700&family=Playfair+Display:wght@800&family=Open+Sans:wght@600;700&family=Arimo&display=swap">
<style>
  :root {
    --page-bg: #eef0f1;
    --pouch-white: #ffffff;
    --leaf-green: #6aa83a;
    --deep-green: #2e6b1f;
    --band-green: #3f8a2a;
    --tomato-red: #c8241c;
    --ink: #2a2a2a;
    --photo-warm: #6b3a26;
    --photo-dark: #4a4530;
  }
  * { box-sizing: border-box; margin: 0; padding: 0; }
  html, body {
    width: 1200px; height: 923px; overflow: hidden;
    background: var(--page-bg);
  }
  .pouch-front {
    position: absolute; left: 323px; top: 189px;
    width: 545px; height: 596px;
    background: var(--pouch-white);
    box-shadow: 0 8px 24px rgba(0,0,0,.12);
    overflow: hidden;
  }
  .pouch-art { position: absolute; inset: 0; }
  .brand-line {
    position: absolute; top: 22px; left: 0; width: 100%;
    display: flex; justify-content: center; align-items: center; gap: 8px;
    font-family: "Fredoka", sans-serif; font-weight: 600; font-size: 19px;
    color: var(--band-green);
  }
  .brand-dot { width: 14px; height: 14px; border-radius: 50%; background: var(--tomato-red); }
  .product-title {
    position: absolute; top: 100px; left: 0; width: 100%;
    text-align: center;
    font-family: "Fredoka", sans-serif; font-weight: 700;
    font-size: 64px; line-height: 64px; letter-spacing: -1px;
    color: var(--leaf-green);
    -webkit-text-stroke: 5px var(--deep-green);
    paint-order: stroke fill;
  }
  .product-subtitle {
    position: absolute; top: 250px; left: 0; width: 100%;
    text-align: center;
    font-family: "Fredoka", sans-serif; font-weight: 500; font-size: 21px;
    color: var(--band-green);
  }
  .callout {
    position: absolute; left: 12px;
    font-family: "Playfair Display", serif; font-weight: 800;
    color: #fff; line-height: 1.05;
  }
  .callout-tradition { top: 312px; font-size: 21px; }
  .callout-cooked { top: 407px; font-size: 21px; }
  .callout-cooked small { display: block; font-size: 15px; margin-top: 4px; }
  .beef-note {
    position: absolute; left: 13px; top: 466px;
    font-family: "Open Sans", sans-serif; font-weight: 600;
    font-size: 12px; line-height: 17.5px; color: var(--ink);
  }
  .net-weight {
    position: absolute; left: 13px; top: 540px;
    font-family: "Arimo", sans-serif; font-size: 15px; color: var(--leaf-green);
  }
  .storage-note {
    position: absolute; left: 13px; top: 566px;
    font-family: "Open Sans", sans-serif; font-weight: 700;
    font-size: 10.5px; color: var(--ink);
  }
</style>
</head>
<body>
  <main class="pouch-front">
    <svg class="pouch-art" width="545" height="596" viewBox="0 0 545 596">
      <defs>
        <linearGradient id="brushGreen" x1="1" y1="0" x2="0" y2="1">
          <stop offset="0" stop-color="#3f8a2a"/>
          <stop offset=".6" stop-color="#79b458"/>
          <stop offset="1" stop-color="#ffffff" stop-opacity="0"/>
        </linearGradient>
        <linearGradient id="photoTone" x1="0" y1="1" x2="1" y2="0">
          <stop offset="0" stop-color="#6b3a26"/>
          <stop offset="1" stop-color="#4a4530"/>
        </linearGradient>
      </defs>
      <path role="img" aria-label="Green brushstroke texture" fill="url(#brushGreen)"
            d="M420 0 H545 V272 C500 270 470 250 460 210 C440 160 470 120 440 80 C425 55 430 25 420 0 Z"/>
      <path class="tradition-badge" fill="var(--band-green)"
            d="M0 292 C40 286 110 270 150 282 C180 292 175 330 160 360 C148 384 120 388 0 388 Z"/>
      <path class="cooked-badge" fill="var(--tomato-red)"
            d="M2 394 H170 C180 396 180 420 172 440 C166 456 150 462 2 465 Z"/>
      <path role="img" aria-label="Photo of a bowl of duck and barley soup on a wooden table" fill="url(#photoTone)"
            d="M175 596 C170 420 320 292 545 290 V596 Z"/>
      <path fill="none" stroke="var(--band-green)" stroke-width="10"
            d="M175 601 C170 420 320 292 550 290"/>
    </svg>

    <div class="brand-line"><span class="brand-dot"></span>Fair Ladle Foods</div>

    <h1 class="product-title">Duck &amp; Barley<br>Soup</h1>
    <p class="product-subtitle">Made with Organic Seaweed</p>

    <p class="callout callout-tradition">Traditional<br>Korean-Style<br>Soup</p>
    <p class="callout callout-cooked">Fully Cooked<small>Ready in Minutes</small></p>

    <p class="beef-note">Beef used<br>raised with<br>no hormones &amp;<br>no antibiotics</p>
    <p class="net-weight">Net Wt. 2 LBs (32oz)</p>
    <p class="storage-note">Keep Refrigerated</p>
  </main>
</body>
</html>
```